PELDRAX Business Cards

We require a business card for our company that provides IT consulting services. We already have a logo that needs to be used on the card. We want a clean professional looking design that incorporates our colours. Our main focus is providing managed services to business, which involves us looking after all of their IT requirements including managing servers/networks, projects, and procurement.

Industry/Entity Type

Information Technology

Requirements
Must have
• our logo, contact information, name, title, phone numbers

```html
<!DOCTYPE html>
<html lang="en">
<head>
<meta charset="utf-8">
<title>PELDRAX Business Card</title>
<link rel="stylesheet" href="https://fonts.googleapis.com/css2?family=Roboto:wght@400;500;700&display=swap">
<style>
  :root {
    --brand-blue: #1493cf;
    --brand-blue-deep: #0f86c2;
    --ink: #4a4a4a;
    --rule: #8a8a8a;
    --swoosh-grey: #7d7d80;
    --paper: #fbfbfb;
    --backdrop: #2c2d31;
  }
  * { box-sizing: border-box; margin: 0; padding: 0; }
  html, body {
    width: 1200px; height: 1200px; overflow: hidden;
    background: var(--backdrop);
    font-family: "Roboto", Arial, sans-serif;
  }
  .canvas { position: relative; width: 1200px; height: 1200px; }

  .card {
    position: absolute; left: 260px;
    width: 680px; height: 388px;
    border-radius: 18px; overflow: hidden;
  }
  .card--front { top: 158px; background: var(--paper); }
  .card--back {
    top: 652px;
    background: linear-gradient(180deg, var(--brand-blue-deep), var(--brand-blue));
    display: flex; align-items: center; justify-content: center;
  }

  .wordmark {
    position: absolute; left: 56px; top: 170px;
    font-weight: 500; font-size: 44px; letter-spacing: 3px;
    color: var(--brand-blue); line-height: 1;
  }
  .divider {
    position: absolute; left: 340px; top: 108px;
    width: 2px; height: 174px; background: var(--rule);
  }
  .details { position: absolute; left: 384px; top: 110px; color: var(--ink); }
  .details__name { font-weight: 500; font-size: 21px; color: var(--brand-blue); line-height: 1.2; }
  .details__title { font-size: 15px; line-height: 1.3; }
  .details__address { margin-top: 18px; font-size: 15px; line-height: 1.35; }
  .details__contacts { margin-top: 14px; list-style: none; font-size: 15.5px; line-height: 1.3; }
  .details__contacts li { display: flex; align-items: center; gap: 10px; }
  .details__contacts svg { width: 12px; height: 12px; flex: none; }

  .swoosh { position: absolute; left: 0; bottom: 0; width: 680px; height: 60px; }

  .back-mark {
    font-weight: 500; font-size: 76px; letter-spacing: 6px;
    color: #fff; line-height: 1;
  }
</style>
</head>
<body>
<main class="canvas">
  <section class="card card--front" aria-label="Card front">
    <div class="wordmark">PELDRAX</div>
    <div class="divider"></div>
    <div class="details">
      <p class="details__name">Daniel Harwick</p>
      <p class="details__title">President</p>
      <p class="details__address">48 Cedar Avenue, PO Box 2710<br>Ridgefield, AB, T4R 1K6</p>
      <ul class="details__contacts">
        <li>
          <svg viewBox="0 0 12 12" aria-hidden="true"><path d="M2.5 1 L4.5 1 L5.2 3.6 L4 4.6 C4.6 6 5.9 7.4 7.4 8 L8.4 6.8 L11 7.5 L11 9.5 C11 10.3 10.3 11 9.5 11 C5 11 1 7 1 2.5 C1 1.7 1.7 1 2.5 1 Z" fill="var(--brand-blue)"/></svg>
          403-555-0182
        </li>
        <li>
          <svg viewBox="0 0 12 12" aria-hidden="true"><rect x="1" y="2.5" width="10" height="7" fill="none" stroke="var(--brand-blue)" stroke-width="1.2"/><path d="M1 2.5 L6 6.5 L11 2.5" fill="none" stroke="var(--brand-blue)" stroke-width="1.2"/></svg>
          info@peldrax.com
        </li>
        <li>
          <svg viewBox="0 0 12 12" aria-hidden="true"><g fill="none" stroke="var(--brand-blue)" stroke-width="1"><circle cx="6" cy="6" r="5"/><ellipse cx="6" cy="6" rx="2.2" ry="5"/><path d="M1 6 H11 M2 3.5 H10 M2 8.5 H10"/></g></svg>
          www.peldrax.com
        </li>
      </ul>
    </div>
    <svg class="swoosh" viewBox="0 0 680 60" preserveAspectRatio="none" aria-hidden="true">
      <path d="M0 60 L0 54 Q340 6 680 54 L680 60 Z" fill="var(--brand-blue)"/>
      <path d="M0 60 L0 56 Q340 16 680 56 L680 60 Z" fill="var(--brand-blue)"/>
      <path d="M40 50 Q340 -8 640 50" fill="none" stroke="var(--swoosh-grey)" stroke-width="3"/>
    </svg>
  </section>

  <section class="card card--back" aria-label="Card back">
    <div class="back-mark">PELDRAX</div>
  </section>
</main>
</body>
</html>
```